New Business Card Design Project

Removed as project is complete.

Target Market(s)

Industry/Entity Type

Business

Requirements
Must have
• Removed as project is complete.
Nice to have
Should not have

```html
<!DOCTYPE html>
<html lang="en">
<head>
<meta charset="utf-8">
<title>Emberline Assurance – Business Cards</title>
<link rel="stylesheet" href="https://fonts.googleapis.com/css2?family=Didact+Gothic&family=PT+Sans:wght@700&display=swap">
<style>
  :root {
    --page-bg: #ffffff;
    --card-dark: #000000;
    --card-light: #ffffff;
    --ink-light: #ffffff;
    --ink-dark: #111111;
    --brand-orange: #f07a1a;
    --band-blue: #1e9be0;
    --band-pink: #d0449c;
    --band-yellow: #f6c100;
    --footer-ink: #000000;
  }
  html, body {
    margin: 0;
    padding: 0;
    width: 1200px;
    height: 960px;
    overflow: hidden;
    background: var(--page-bg);
  }
  .canvas {
    position: relative;
    width: 1200px;
    height: 960px;
  }
  .card {
    position: absolute;
    left: 172px;
    width: 824px;
    height: 390px;
    border-radius: 18px;
    overflow: hidden;
    font-family: "Didact Gothic", "Century Gothic", sans-serif;
  }
  .card--dark { top: 36px; background: var(--card-dark); color: var(--ink-light); }
  .card--light { top: 456px; background: var(--card-light); color: var(--ink-dark); }
  .card__band {
    position: absolute;
    left: 0;
    bottom: 0;
    width: 100%;
    height: 74px;
    background: linear-gradient(180deg, var(--band-blue) 0%, var(--band-pink) 22%, var(--band-yellow) 42%, var(--band-yellow) 100%);
  }
  .brand {
    position: absolute;
    display: flex;
    align-items: center;
    gap: 12px;
    color: var(--brand-orange);
    font-size: 34px;
    letter-spacing: -0.5px;
  }
  .brand__mark {
    width: 46px; height: 46px;
    background: var(--brand-orange);
  }
  .card--dark .brand { left: 28px; top: 28px; }
  .card--light .brand { left: 18px; top: 22px; }
  .contact__line {
    position: absolute;
    margin: 0;
    white-space: nowrap;
    line-height: 1;
  }
  .contact__name { font-size: 33px; letter-spacing: 1.5px; word-spacing: -4px; }
  .contact__detail { font-size: 30.5px; }
  .contact__mobile { letter-spacing: 2px; word-spacing: 2px; }
  .contact__email { letter-spacing: 0.7px; }
  .contact__web { letter-spacing: 0.3px; }
  .card--dark .contact__name { left: 128px; top: 128px; }
  .card--dark .contact__mobile { left: 142px; top: 168px; }
  .card--dark .contact__email { left: 148px; top: 206px; }
  .card--dark .contact__web { left: 212px; top: 246px; }
  .card--light .contact__name { left: 190px; top: 134px; }
  .card--light .contact__mobile { left: 204px; top: 174px; }
  .card--light .contact__email { left: 210px; top: 212px; }
  .card--light .contact__web { left: 274px; top: 252px; }
  .card__footer {
    position: absolute;
    left: 12px;
    bottom: 10px;
    margin: 0;
    font-family: "PT Sans", Verdana, sans-serif;
    font-weight: 700;
    font-size: 21px;
    letter-spacing: 0.9px;
    color: var(--footer-ink);
    white-space: nowrap;
  }
</style>
</head>
<body>
<main class="canvas">

  <section class="card card--dark">
    <div class="card__band" role="img" aria-label="Decorative colour band in blue, pink and yellow along the bottom edge"></div>
    <div class="brand"><span class="brand__mark"></span><span class="brand__name">emberline assurance</span></div>
    <p class="contact__line contact__name">Persons Name</p>
    <p class="contact__line contact__detail contact__mobile">Person's Mobile: +61 (0)987 654 321</p>
    <p class="contact__line contact__detail contact__email">email: name@emberlineassurance.com</p>
    <p class="contact__line contact__detail contact__web">www.emberlineassurance.com</p>
    <p class="card__footer">Emberline Assurance International Pty Ltd P.O. Box 2187, Harbour Vale NSW 2098</p>
  </section>

  <section class="card card--light">
    <div class="card__band" role="img" aria-label="Decorative colour band in blue, pink and yellow along the bottom edge"></div>
    <div class="brand"><span class="brand__mark"></span><span class="brand__name">emberline assurance</span></div>
    <p class="contact__line contact__name">Persons Name</p>
    <p class="contact__line contact__detail contact__mobile">Person's Mobile: +61 (0)987 654 321</p>
    <p class="contact__line contact__detail contact__email">email: name@emberlineassurance.com</p>
    <p class="contact__line contact__detail contact__web">www.emberlineassurance.com</p>
    <p class="card__footer">Emberline Assurance International Pty Ltd P.O. Box 2187, Harbour Vale NSW 2098</p>
  </section>

</main>
</body>
</html>
```